Brochure Design Project

Need a new look. Customer wants to update 10 year old literature. Very similar "text content" and color scheme only. Need a new modern look. Clean fonts...maybe distressed fonts. Nice salon. Would like brochure to be consistent with their decor...possibly "curvey" graphics maybe simple die-cut if cost effective to produce. Use your imagination! Showed them some pixel harbor work that they liked the look of and I will share these details so you have a feel for the type of work we are looking for.

Reason: My customer has reviewed the art submissions and though she likes the ideas presented, she has indicated that she needs to stay more consistent with some other collateral which means she would prefer a more mono-chromatic (maybe two or three colors but not a full color glossy brochure. Keeping in mind that she would like a matte look please offer design selections. She has sent me some images of the other collateral she would possibly like to coordinate with which I can send via email upon request.

Target Market(s)

Salon Patrons

Industry/Entity Type

Salon

Requirements
Must have
• Packaged InDesign file upon completion so we can edit down the line(update prices etc.) High Res PDF with marks and bleeds. Must fit into No. 10 envelope(4.125" x 9.5") once folded...I am thinking 9x16 but am open to ideas.
Should not have
• photos...or limit

```html
<!DOCTYPE html>
<html lang="en">
<head>
<meta charset="utf-8">
<title>Lumen Salon Spa – Brochure</title>
<link rel="stylesheet" href="https://fonts.googleapis.com/css2?family=Open+Sans:ital,wght@0,400;0,600;0,700;0,800;1,600&display=swap">
<style>
  :root{
    --bg:#dcdcd8;
    --paper:#c9d72b;
    --paper-light:#d9e54a;
    --paper-deep:#aebd14;
    --ink:#24270c;
    --ink-soft:#3c4114;
    --wave:rgba(255,255,255,.22);
  }
  *{box-sizing:border-box;margin:0;padding:0}
  html,body{width:1200px;height:963px;overflow:hidden;background:var(--bg);font-family:"Open Sans",Arial,sans-serif;color:var(--ink)}
  .canvas{position:relative;width:1200px;height:963px}
  .spread{position:absolute;left:22px;top:221px;width:900px;height:520px;display:flex;box-shadow:0 6px 18px rgba(0,0,0,.25)}
  .cover{position:absolute;left:952px;top:221px;width:225px;height:520px;box-shadow:0 6px 18px rgba(0,0,0,.25)}
  .panel{position:relative;width:225px;height:520px;overflow:hidden;
    background:radial-gradient(ellipse at 50% 35%,var(--paper-light),var(--paper) 60%,var(--paper-deep));
    padding:26px 16px 16px}
  .panel + .panel{border-left:1px solid rgba(0,0,0,.08)}
  .waves{position:absolute;inset:0;width:100%;height:100%;pointer-events:none}
  .content{position:relative}
  h2{font-weight:800;font-size:17px;letter-spacing:.5px;text-transform:uppercase;text-align:center;margin:10px 0 8px}
  h2.left{text-align:left;font-size:13px;margin:8px 0 4px}
  .note{font-size:6.5px;line-height:1.35;color:var(--ink-soft);margin-bottom:8px}
  .package{display:flex;gap:8px;margin-bottom:9px}
  .dot{flex:0 0 11px;height:11px;border-radius:50%;background:var(--ink);margin-top:6px;box-shadow:inset 0 0 0 2.5px var(--paper),inset 0 0 0 4px var(--ink)}
  .package-name{font-size:7.5px;font-weight:600;font-style:italic}
  .package-desc{font-size:8px;line-height:1.25}
  .package-time{font-size:6.5px;color:var(--ink-soft)}
  .policy{text-align:center;margin-bottom:6px}
  .policy h3{font-size:9px;font-weight:600;font-style:italic;margin-bottom:2px}
  .policy p{font-size:6.4px;line-height:1.35}
  .rule{height:1px;background:var(--ink);opacity:.7;margin:7px 10px}
  .team{font-size:7.8px;line-height:1.4;text-align:center;margin-bottom:7px}
  .brand{display:flex;align-items:center;justify-content:center;gap:6px;margin:4px 0 16px;white-space:nowrap}
  .brand-mark{flex:0 0 12px;width:12px;height:12px;border-radius:50%;background:#fff}
  .brand-name{font-weight:800;font-size:17px;color:#fff;letter-spacing:.3px}
  .cover .brand{margin:120px 0 6px}
  .cover .brand-name{font-size:18px}
  .brand-rule{height:1.5px;background:#fff;margin:0 8px 12px}
  .body{font-size:8px;line-height:1.45;text-align:justify;margin-bottom:9px}
  .body b{font-weight:700}
  .hours{text-align:center;margin-top:12px}
  .hours h2{font-size:12px;margin:0 0 3px}
  .hours p{font-size:6.8px;font-weight:600;line-height:1.35}
  .hours .addr{font-weight:400;border-top:1px solid var(--ink);margin-top:4px;padding-top:4px}
  .contact{position:absolute;left:16px;right:16px;font-size:6.8px;line-height:1.4;text-align:right}
  .contact b{font-weight:700}
  .directions{position:absolute;left:14px;right:14px;bottom:14px;font-size:6.2px;line-height:1.4}
</style>
</head>
<body>
<div class="canvas">

  <section class="spread" aria-label="Brochure inside spread">
    <article class="panel panel-packages">
      <svg class="waves" viewBox="0 0 225 520" preserveAspectRatio="none"><path d="M0 430 C60 400 150 470 225 420 L225 520 L0 520Z" fill="var(--wave)"/></svg>
      <div class="content">
        <h2 class="left">Spa Packages</h2>
        <p class="note">*All times are approximate. Dressing time and a complimentary foot soak are included.</p>
        <div class="package"><span class="dot"></span><div><div class="package-name">take a break</div><div class="package-desc">Express Facial and Half Hour Massage</div><div class="package-time">*Approximately 1 1/2 hours $100</div></div></div>
        <div class="package"><span class="dot"></span><div><div class="package-name">couples escape</div><div class="package-desc">Two people receive a Full Body Massage in our couples suite.</div><div class="package-time">*Approximately 1 1/2 hours $140</div></div></div>
        <div class="package"><span class="dot"></span><div><div class="package-name">taste of pampering</div><div class="package-desc">Half-Hour Massage, Express Facial and Pedicure</div><div class="package-time">*Approximately 2 1/2 hours $164</div></div></div>
        <div class="package"><span class="dot"></span><div><div class="package-name">lumen afternoon getaway</div><div class="package-desc">Scrub or Wrap, Full Body Massage, Customized Facial and Lunch.</div><div class="package-time">*Approximately 2 1/2 hours $164</div></div></div>
        <div class="package"><span class="dot"></span><div><div class="package-name">lumen mental retreat</div><div class="package-desc">Scrub, Wrap, Full Body Massage, Customized Facial and Lunch</div><div class="package-time">*Approximately 4 hours $240</div></div></div>
        <div class="package"><span class="dot"></span><div><div class="package-name">our afternoon rendezvous</div><div class="package-desc">Two people enjoy a Scrub or Wrap, Full Body Massage, Customized Facial and Lunch.</div><div class="package-time">*Approximately 3 1/2 hours $380</div></div></div>
        <div class="package"><span class="dot"></span><div><div class="package-name">imagine the experience</div><div class="package-desc">Scrub, Wrap, Full Body Massage, Customized Facial, Hot Stone Massage, Spa Manicure, Spa Pedicure, Hair Cut and Style, and Lunch.</div><div class="package-time">*Approximately 4 hours $240</div></div></div>
        <div class="package"><span class="dot"></span><div><div class="package-name">create your own experience</div><div class="package-desc">Choose any combination of your favorite spa experiences and let us do the rest to make it a day to remember.</div><div class="package-time">A value of $190 or more includes a complimentary lunch during your visit.</div></div></div>
      </div>
    </article>

    <article class="panel panel-about">
      <svg class="waves" viewBox="0 0 225 520" preserveAspectRatio="none"><path d="M0 0 L225 0 L225 60 C160 110 70 20 0 70Z" fill="var(--wave)"/></svg>
      <div class="content">
        <h2>About Us</h2>
        <div class="policy"><h3>children</h3><p>For insurance and safety reasons, children are not permitted in any service area of the salon or spa unless having a service performed.</p></div>
        <div class="policy"><h3>cell phones</h3><p>For the courtesy of our guests we ask that your cell phone be turned to vibrate or off. Cell phones are not permitted in the spa.</p></div>
        <div class="policy"><h3>pricing</h3><p>All prices are subject to change without notice.</p></div>
        <div class="policy"><h3>cancellation</h3><p>At lumen salon and spa, we require a 24-hour cancellation notice.</p></div>
        <div class="policy"><h3>multiple services</h3><p>For multiple services, bridal parties and spa packages we do require a credit card number for confirmation. In the event you miss your scheduled appointment, charges will be applied to your card.</p></div>
        <div class="policy"><h3>retail returns</h3><p>No cash refunds. Exchanges only on all retail items excluding brushes and makeup which are non-returnable.</p></div>
        <div class="policy"><h3>gift certificates</h3><p>Gift certificates are available in any denomination. For your convenience, gift certificates can be purchased on line at www.lumensalonspa.com. All gift certificates are non-refundable and carry their value for one year.</p></div>
        <div class="rule"></div>
        <p class="team">We are proud to have a team of wonderful people who are dedicated to self-growth, continued education and who have a strong desire to make people look and feel better. When you look good, you feel good.</p>
        <p class="team">Our staff is committed to serving our guests as a team. We encourage trying our various technicians in order to enjoy all of their wonderful talents and ideas.</p>
      </div>
    </article>

    <article class="panel panel-welcome">
      <svg class="waves" viewBox="0 0 225 520" preserveAspectRatio="none"><path d="M0 120 C70 60 150 150 225 90 L225 0 L0 0Z" fill="var(--wave)"/></svg>
      <div class="content">
        <div class="brand"><span class="brand-mark"></span><span class="brand-name">Lumen Salon Spa</span></div>
        <p class="body"><b><i>Communication is the key</i></b> to a successful relationship with our clients. If at any time you are uncomfortable or dissatisfied in any way, we promise to make every effort to remedy the situation. Your opinions and comments are vital to the growth and success of our business and are greatly appreciated. If, for any reason, you are unhappy with a lumen salon product, we will gladly exchange it with an equal product more suitable to your needs.</p>
        <p class="body">To ensure you get the appointment time you most desire, we encourage you to book your next appointment before leaving.</p>
        <p class="body">In the event that you cannot make your scheduled appointment we ask that you give us a 24-hour cancellation notice so that we may accommodate another lumen salon and spa client.</p>
        <div class="hours">
          <h2>Salon Hours</h2>
          <p>Monday &amp; Wednesday 9-8<br>Tuesday &amp; Thursday 9-9<br>Friday 9-7<br>Saturday 9-5</p>
          <p class="addr">4120 orchard pike, milford<br>kentucky 41099 USA<br>859 555 0142<br>www.<b>lumensalonspa</b>.com<br>hello@lumensalonspa.com</p>
        </div>
      </div>
    </article>

    <article class="panel panel-flap">
      <svg class="waves" viewBox="0 0 225 520" preserveAspectRatio="none"><path d="M0 40 C80 0 140 110 225 50 L225 0 L0 0Z" fill="var(--wave)"/><path d="M0 300 C90 250 140 360 225 310 L225 520 L0 520Z" fill="rgba(255,255,255,.12)"/></svg>
      <p class="contact" style="top:300px">859 555 0142<br>www.<b>lumensalonspa</b>.com<br>hello@lumensalonspa.com</p>
      <p class="directions">Directions: From Riverton, take I-75 to the Orchard Pike Exit (180). Left off the exit. On the right, less than a half mile will be lumen salon and spa. From the south, take exit 180, turn right onto Orchard Pike, and find us on the right, just past the light.</p>
    </article>
  </section>

  <article class="panel cover" aria-label="Brochure front cover">
    <svg class="waves" viewBox="0 0 225 520" preserveAspectRatio="none"><path d="M0 60 C70 20 140 120 225 40 L225 0 L0 0Z" fill="var(--wave)"/><path d="M0 420 C80 380 150 470 225 410 L225 520 L0 520Z" fill="rgba(255,255,255,.12)"/></svg>
    <div class="content">
      <div class="brand"><span class="brand-mark"></span><span class="brand-name">Lumen Salon Spa</span></div>
      <div class="brand-rule"></div>
      <p class="body">At <b>lumen salon and spa</b> we are dedicated to making every visit a positive experience. Whether you are here for a day of pampering or for your regular salon appointment, our staff of experienced professionals are dedicated to meeting your every need. Escape the stresses of life and discover a new environment of relaxation and beauty.</p>
    </div>
    <p class="contact" style="top:440px">859 555 0142<br>www.<b>lumensalonspa</b>.com<br>hello@lumensalonspa.com</p>
  </article>

</div>
</body>
</html>
```